Medical Billing - Professional Marketing Flier

We are needing help designing a clean and professional looking easy to read marketing flier for a medical billing practice. The text needs to be large enough to print. We are looking for a 5.5 x 8.5 design that we can edit the text as needed. I have included our logo and what we initially want it to say. Please keep in mind, we also want our logo and contact details on the flier. Let me know if you have any questions.

```html
<!DOCTYPE html>
<html lang="en">
<head>
<meta charset="utf-8">
<title>Vega Medical Billing – Flier</title>
<link href="https://fonts.googleapis.com/css2?family=Lato:wght@400;700;900&display=swap" rel="stylesheet">
<style>
  :root {
    --sky: #7fd0ef;
    --sky-deep: #2e8fc4;
    --orchid: #c96fb0;
    --orchid-deep: #9a5bb0;
    --headline-pink: #c565a6;
    --teal-ink: #174a66;
    --body-ink: #2b2b2b;
    --muted-ink: #555a60;
    --rule: #7b7398;
    --paper: #ffffff;
  }
  * { box-sizing: border-box; margin: 0; padding: 0; }
  html, body { width: 828px; height: 1200px; overflow: hidden; background: var(--paper); }
  body { font-family: "Lato", Arial, sans-serif; color: var(--body-ink); }
  .flier { position: relative; width: 828px; height: 1200px; overflow: hidden; background: var(--paper); }

  .backdrop-photo {
    position: absolute; left: 260px; top: 400px; width: 568px; height: 360px;
    background: radial-gradient(ellipse at 60% 35%, rgba(200,205,210,0.55), rgba(235,238,240,0.35) 55%, rgba(255,255,255,0) 80%);
  }
  .hero-photo { position: absolute; left: 0; top: 0; width: 540px; height: 500px; }

  .tagline-disc {
    position: absolute; left: 418px; top: 212px; width: 292px; height: 288px; border-radius: 50%;
    background: radial-gradient(circle at 35% 30%, #d58ac0, var(--orchid) 55%, var(--orchid-deep));
    opacity: 0.95;
    display: flex; align-items: center; justify-content: center; text-align: center;
  }
  .tagline-disc h1 {
    color: #fff; font-weight: 700; font-size: 39px; line-height: 46px; letter-spacing: 0.3px;
  }

  .brand {
    position: absolute; left: 580px; top: 128px; display: flex; align-items: center; gap: 10px;
    color: var(--orchid-deep); font-weight: 700; font-size: 19px; line-height: 22px; letter-spacing: 1.5px;
  }
  .brand-dot { width: 14px; height: 14px; border-radius: 50%; background: var(--orchid-deep); flex: none; }

  .intro {
    position: absolute; left: 40px; top: 540px; width: 240px;
    color: var(--headline-pink); font-weight: 700; font-size: 24px; line-height: 30px;
  }

  .services {
    position: absolute; left: 304px; top: 534px; width: 492px; height: 492px;
    column-count: 2; column-gap: 26px; column-fill: auto;
  }
  .service h2 {
    color: var(--teal-ink); font-weight: 700; font-size: 19px; line-height: 23px; letter-spacing: 0.3px;
    margin-bottom: 3px; break-after: avoid;
  }
  .service p {
    font-size: 14px; line-height: 19.4px; text-align: justify; hyphens: auto;
  }
  .service + .service { margin-top: 14px; }
  .service--credentialing { break-before: auto; }

  .divider { position: absolute; left: 40px; top: 1043px; width: 749px; height: 1px; background: var(--rule); }
  .contact { position: absolute; left: 40px; top: 1056px; width: 749px; text-align: center; }
  .contact h2 { color: var(--teal-ink); font-weight: 700; font-size: 21px; line-height: 26px; margin-bottom: 5px; }
  .contact p { color: var(--muted-ink); font-size: 12.2px; line-height: 15.6px; }
  .contact-line {
    position: absolute; left: 40px; top: 1152px; width: 749px; text-align: center;
    font-weight: 700; font-size: 15.4px; color: #111; white-space: nowrap;
  }
</style>
</head>
<body>
<main class="flier">
  <div class="backdrop-photo" role="img" aria-label="Faded black and white photo of hands writing on a clipboard beside a tablet"></div>

  <svg class="hero-photo" viewBox="0 0 540 500" role="img" aria-label="Blue-toned photo of a smiling doctor embracing an older patient, overlaid with thin connecting lines">
    <defs>
      <linearGradient id="heroTone" x1="0" y1="0" x2="1" y2="1">
        <stop offset="0" stop-color="#4fa9d8"/>
        <stop offset="0.5" stop-color="#7fcbeb"/>
        <stop offset="1" stop-color="#2f86bd"/>
      </linearGradient>
    </defs>
    <path d="M0 0 H482 C540 90 545 230 470 330 C400 430 260 500 110 497 C70 496 30 485 0 462 Z" fill="url(#heroTone)"/>
  </svg>

  <div class="tagline-disc">
    <h1>FOCUS<br>ON WHAT<br>MATTERS<br>MOST</h1>
  </div>

  <div class="brand">
    <span class="brand-dot"></span>
    <span>VEGA<br>MEDICAL BILLING</span>
  </div>

  <p class="intro">The staff at VEGA MEDICAL BILLING truly care about your success. We want to assist and support you to help take the confusion out of medical billing. We go the extra mile to make sure your revenue cycle continues to flow even when issues arise.</p>

  <div class="services">
    <section class="service">
      <h2>MEDICAL BILLING</h2>
      <p>Would you prefer to spend time focusing on your clients and running your practice rather than trying to stay up to speed with the constantly changing medical billing rules and regulations? Let us help you by managing your medical billing and dealing with the insurance companies on your behalf! We work with you to tailor the entire medical billing process to suit your practices needs while making it as smooth and painless as possible.</p>
    </section>
    <section class="service">
      <h2>AGING</h2>
      <p>Are you leaving money on the table? Are you able to do the follow-through needed to keep your aging in check and more money flowing into your practice? Are you uncertain about how to get insurance to pay on claims that should be covered but for some reason they decided not to? We can clean up your aging, reduce the amount of time it takes for claims to pay out, and we can keep your aging to a minimum.</p>
    </section>
    <section class="service service--credentialing">
      <h2>CREDENTIALING</h2>
      <p>Are you wanting to get contracted with insurance companies but aren’t sure how to go about it? Are you wanting to expand your client base by having the option to bill insurance? Let us take the confusion out of what can seem like a daunting task! We can get you and your practitioners contracted with the insurance companies of your choice and help you navigate through the process every step of the way!</p>
    </section>
  </div>

  <div class="divider"></div>
  <section class="contact">
    <h2>CONTACT US</h2>
    <p>If any of these processes are something you would like our help with or to consult with us on, please email us or give us a call! We specialize in billing and contracting for Nutritionists and Dietitians. We would love to help you expand your business and take the pain and frustration out of billing so you can focus on your clients.</p>
  </section>
  <p class="contact-line">T: 555-014-2290 • E: admin@vegamedicalbilling.com • PO Box 418 Cedar Falls, WA 98099</p>
</main>
</body>
</html>
```